Studio Business Cards etc
business cards plus
Creative Brief
Use same font as used in my logo
The font Iuse in my log is called "Presidential.ttf"
Modern
Dana Holcrofter
Owner / Cheif Instructor
20381 Brenwick Lane NW #214 Silverdale WA 98383
qplrt@exmailbox.net
http://www.kestonhallstudio.com
I am looking for a new style of layout for my business cards etc. I would be interested in seeing a layout for the standard 3.5x2 as well as a folded card 3.5x 4 The inside could be used for class schedule etc. The name / title would of course be changed depending on our instructors
Concepts
Business card and stationary design. We provide umpires & referees for teams/organizations.

```html
<!DOCTYPE html>
<html lang="en">
<head>
<meta charset="utf-8">
<title>Keston Hall Martial Arts – Stationery Set</title>
<link href="https://fonts.googleapis.com/css2?family=Open+Sans:wght@400;600&display=swap" rel="stylesheet">
<style>
  :root{
    --red:#cf1430;
    --red-dark:#a80f26;
    --grey:#6d6e71;
    --grey-light:#bdbec0;
    --paper:#ffffff;
    --ink:#4a4a4c;
    --bg:#ffffff;
    --shadow:0 2px 8px rgba(0,0,0,.22);
  }
  *{box-sizing:border-box;margin:0;padding:0}
  html,body{width:1200px;height:936px;overflow:hidden;background:var(--bg)}
  body{position:relative;font-family:"Open Sans",Arial,sans-serif;color:var(--ink)}
  .sheet{position:absolute;background:var(--paper);box-shadow:var(--shadow);overflow:hidden}
  .sheet svg.edge{position:absolute;inset:0;width:100%;height:100%}

  .brand{position:absolute;display:flex;flex-direction:column;align-items:center;text-align:center}
  .brand-circle{border-radius:50%;border:2px solid var(--red);background:#f1f1f2}
  .brand-name{font-family:"Open Sans",Arial,sans-serif;font-weight:600;color:var(--grey);line-height:1.15;margin-top:4px}

  .letterhead{left:190px;top:51px;width:381px;height:560px}
  .letterhead .brand{left:28px;top:26px;width:90px}
  .letterhead .brand-circle{width:46px;height:46px}
  .letterhead .brand-name{font-size:8px}
  .contact-block{position:absolute;font-size:6.5px;line-height:1.6;color:var(--grey)}
  .letterhead .contact-block{left:172px;top:28px}
  .watermark{position:absolute;left:60px;top:200px;width:200px;opacity:.18}
  .watermark .brand-circle{width:120px;height:120px}
  .watermark .brand-name{font-size:15px}

  .folder{left:634px;top:38px;width:381px;height:576px}
  .folder .brand{left:70px;top:200px;width:190px}
  .folder .brand-circle{width:120px;height:120px}
  .folder .brand-name{font-size:15px}

  .card-front{left:56px;top:655px;width:137px;height:81px}
  .card-front .brand{left:10px;top:10px;width:46px}
  .card-front .brand-circle{width:24px;height:24px;border-width:1.5px}
  .card-front .brand-name{font-size:4.5px}
  .card-name{position:absolute;left:66px;top:12px;font-size:6px;font-weight:600;color:var(--red)}
  .card-title{position:absolute;left:66px;top:20px;font-size:4.2px;color:var(--grey)}
  .card-front .contact-block{left:66px;top:36px;font-size:4.2px;line-height:1.55}

  .card-back{left:56px;top:753px;width:137px;height:84px;background:var(--red)}
  .card-back .brand{left:33px;top:12px;width:70px;opacity:.35}
  .card-back .brand-circle{width:40px;height:40px;border-color:#fff;background:transparent}
  .card-back .brand-name{font-size:6.5px;color:#fff}

  .envelope-front{left:256px;top:662px;width:447px;height:185px}
  .envelope-front .brand{left:18px;top:10px;width:96px}
  .envelope-front .brand-circle{width:46px;height:46px}
  .envelope-front .brand-name{font-size:8px}
  .envelope-front .contact-block{left:22px;top:92px;font-size:6.5px}

  .envelope-back{left:736px;top:667px;width:411px;height:180px}
  .flap-url{position:absolute;left:0;right:0;top:16px;text-align:center;color:#fff;font-size:11px;letter-spacing:.3px}
</style>
</head>
<body>

<section class="sheet letterhead" aria-label="Letterhead">
  <svg class="edge" viewBox="0 0 381 560" preserveAspectRatio="none">
    <path d="M352 0 Q320 280 332 560 L381 560 L381 0 Z" fill="var(--red)"/>
    <path d="M338 0 Q306 280 318 560" fill="none" stroke="var(--grey)" stroke-width="5"/>
  </svg>
  <div class="brand">
    <div class="brand-circle"></div>
    <div class="brand-name">Keston Hall<br>Martial Arts</div>
  </div>
  <div class="contact-block">
    20381 Brenwick Lane NW #214<br>
    Silverdale WA 98383<br>
    Tel: 360.555.0142<br>
    qplrt@exmailbox.net<br>
    http://www.kestonhallstudio.com
  </div>
  <div class="brand watermark">
    <div class="brand-circle"></div>
    <div class="brand-name">Keston Hall<br>Martial Arts</div>
  </div>
</section>

<section class="sheet folder" aria-label="Presentation folder">
  <svg class="edge" viewBox="0 0 381 576" preserveAspectRatio="none">
    <path d="M345 0 Q300 300 318 576 L381 576 L381 0 Z" fill="var(--red)"/>
    <path d="M331 0 Q286 300 304 576" fill="none" stroke="var(--grey)" stroke-width="5"/>
  </svg>
  <div class="brand">
    <div class="brand-circle"></div>
    <div class="brand-name">Keston Hall<br>Martial Arts</div>
  </div>
</section>

<section class="sheet card-front" aria-label="Business card front">
  <svg class="edge" viewBox="0 0 137 81" preserveAspectRatio="none">
    <path d="M0 0 L8 0 Q3 40 6 81 L0 81 Z" fill="var(--red)"/>
  </svg>
  <div class="brand">
    <div class="brand-circle"></div>
    <div class="brand-name">Keston Hall<br>Martial Arts</div>
  </div>
  <div class="card-name">Dana Holcrofter</div>
  <div class="card-title">Owner / Chief Instructor</div>
  <div class="contact-block">
    20381 Brenwick Lane NW #214<br>
    Silverdale WA 98383<br>
    Tel: 360.555.0142<br>
    qplrt@exmailbox.net
  </div>
</section>

<section class="sheet card-back" aria-label="Business card back">
  <div class="brand">
    <div class="brand-circle"></div>
    <div class="brand-name">Keston Hall Martial Arts</div>
  </div>
</section>

<section class="sheet envelope-front" aria-label="Envelope front">
  <div class="brand">
    <div class="brand-circle"></div>
    <div class="brand-name">Keston Hall<br>Martial Arts</div>
  </div>
  <div class="contact-block">
    20381 Brenwick Lane NW #214<br>
    Silverdale WA 98383
  </div>
</section>

<section class="sheet envelope-back" aria-label="Envelope back">
  <svg class="edge" viewBox="0 0 411 180" preserveAspectRatio="none">
    <path d="M0 0 L411 0 L411 46 Q205 64 0 46 Z" fill="var(--red)"/>
  </svg>
  <div class="flap-url">www.kestonhallstudio.com</div>
</section>

</body>
</html>
```